Quelvo service sheets and folder

A set of 12 Service sheets plus a rate card to be inserted into a folder - each to be designed and formatted.
A4
Portrait
- the idea is to keep things simple and crisp.
I would use the logo (see attached .ai file) at the top and maybe an separate image to go with each sheet

Around 350 words per page (see attached example)
The format is mainly text and bullet points, but each page will be same layout (just a different image as indicated above).

Need to factor in a folder to hold the service sheets.

The documents to have a good sales impact and your experience and advice on best ideas would be welcome. The key is to keep it crisp, elegant & professional for financial services.

The output files should be in PDF and raw file formats so that printing can be managed easily in future., Details for my new Catalogue Design Project will be added soon.

Industry/Entity Type

Financial

Requirements
Must have
• Inspire us!
Should not have
• No images of people or parts (like hands, arms) etc

```html
<!DOCTYPE html>
<html lang="en">
<head>
<meta charset="utf-8">
<title>Quelvo service sheets and folder</title>
<link href="https://fonts.googleapis.com/css2?family=Source+Sans+3:wght@400;600&display=swap" rel="stylesheet">
<style>
:root{
  --backdrop:#8c8c87;
  --paper:#ffffff;
  --ink:#2b2b2b;
  --ink-soft:#555555;
  --brand:#3a3a3a;
  --navy:#173a5e;
  --band:rgba(235,235,235,.88);
  --font:"Source Sans 3", Arial, sans-serif;
}
*{box-sizing:border-box;margin:0;padding:0}
html,body{width:1200px;height:2450px;overflow:hidden}
body{background:var(--backdrop);font-family:var(--font);color:var(--ink);position:relative}
.panel{position:absolute;background:var(--paper);overflow:hidden;box-shadow:0 2px 6px rgba(0,0,0,.18)}
.brand{position:absolute;display:flex;align-items:center;gap:8px;font-family:var(--font);font-weight:600;color:var(--brand);letter-spacing:.5px}
.brand-dot{width:30px;height:30px;border-radius:50%;background:#c8173f}
.url{position:absolute;font-size:13px;color:var(--ink-soft)}

/* front cover */
.cover-front{left:45px;top:41px;width:543px;height:765px}
.cover-front .brand{right:48px;top:86px;font-size:24px}
.cover-headline{position:absolute;left:110px;top:156px;font-size:19px;font-weight:600;color:var(--ink)}
.cover-photo{position:absolute;left:0;top:199px;width:100%;height:566px;
  background:linear-gradient(160deg,#9fb3c6 0%,#6b7784 35%,#b02a4a 55%,#4f9a3a 75%,#3d3f48 100%)}
.cover-intro{position:absolute;left:0;top:199px;width:100%;height:44px;background:var(--band);
  padding:7px 0 0 110px;font-size:11px;line-height:14px;color:var(--ink-soft)}
.cover-footer{position:absolute;left:0;bottom:0;width:100%;height:34px;background:var(--band)}
.cover-footer .url{left:110px;top:9px}

/* inside spread */
.inside-left{left:45px;top:840px;width:543px;height:765px}
.inside-left .brand{left:40px;top:80px;font-size:23px}
.about{position:absolute;left:62px;top:150px;width:400px;font-size:10.5px;line-height:15px;color:var(--ink-soft)}
.about p{margin-bottom:14px}
.about ul{list-style:none;margin:2px 0 14px}
.about li::before{content:"•";margin-right:8px;color:var(--ink)}
.about strong{font-weight:600;color:var(--ink)}
.petals{position:absolute;left:0;bottom:0;width:320px;height:170px;
  background:radial-gradient(ellipse at 10% 100%,rgba(214,84,120,.45),rgba(230,225,120,.35) 45%,rgba(120,190,110,.25) 65%,rgba(255,255,255,0) 80%)}
.inside-left .url{left:112px;bottom:20px}

.inside-right{left:591px;top:840px;width:559px;height:765px;background:#f4f4f4}
.sheet{position:absolute;left:29px;top:12px;width:514px;height:753px;background:var(--paper);box-shadow:0 0 4px rgba(0,0,0,.15)}
.sheet-bar{position:absolute;left:19px;top:0;width:423px;height:13px;background:var(--navy)}
.sheet .brand{left:48px;top:74px;font-size:17px}
.sheet .brand-dot{width:22px;height:22px}
.sheet-photo{position:absolute;left:48px;top:137px;width:423px;height:211px;
  background:linear-gradient(180deg,#0d2a44 0%,#2f7fb0 45%,#6fbde0 65%,#0f3d5c 100%)}
.sheet-title{position:absolute;left:48px;top:412px;font-size:17px;font-weight:600;color:var(--ink)}
.sheet-sub{position:absolute;left:48px;top:472px;font-size:16px;font-weight:600;line-height:20px;color:var(--ink)}
.sheet-copy{position:absolute;left:48px;top:519px;width:420px;font-size:10px;line-height:14px;color:var(--ink-soft)}
.pocket{position:absolute;left:0;top:0;width:559px;height:765px}

/* back cover */
.cover-back{left:608px;top:1637px;width:542px;height:763px}
.cover-back .brand{left:38px;top:590px;font-size:24px}
.contact{position:absolute;left:110px;top:646px;font-size:8.5px;line-height:11px;color:var(--ink-soft)}
.contact p{margin-bottom:8px}
.contact strong{font-weight:600;color:var(--ink)}
</style>
</head>
<body>

<section class="panel cover-front">
  <div class="brand"><span class="brand-dot"></span>Quelvo</div>
  <h1 class="cover-headline">Bespoke financial services tailored for your needs</h1>
  <div class="cover-photo" role="img" aria-label="City office towers seen from street level with coloured glass overlays"></div>
  <p class="cover-intro">Whether you are experienced in financial services or simply wish to<br>appoint an expert Quelvo provide a one stop service for all your needs.</p>
  <div class="cover-footer"><span class="url">www.quelvo.com</span></div>
</section>

<section class="panel inside-left">
  <div class="brand"><span class="brand-dot"></span>Quelvo</div>
  <div class="about">
    <p>Quelvo is a specialist wealth management practice that caters for individual and corporate investors globally.</p>
    <p>Quelvo's team of experts provide a one stop service for all your investment needs. The team has the collective knowledge and experience that rivals any of the best in the market. Most importantly you always have the special attention of one personal trusted adviser but the combined knowledge and experience of the whole firm.</p>
    <strong>You get:</strong>
    <ul>
      <li>Expert Advice</li>
      <li>A tailored approach</li>
      <li>Measurable Results</li>
      <li>Best Market Access</li>
      <li>Multi-Asset investment strategies</li>
    </ul>
    <p>You do not have to tackle unfamiliar markets alone or seek multiple service providers to achieve your ambitions.</p>
  </div>
  <div class="petals" role="img" aria-label="Soft translucent petal shapes in pink, yellow and green"></div>
  <span class="url">www.quelvo.com</span>
</section>

<section class="panel inside-right">
  <article class="sheet">
    <div class="sheet-bar"></div>
    <div class="brand"><span class="brand-dot"></span>Quelvo</div>
    <div class="sheet-photo" role="img" aria-label="Financial district skyline at dusk reflected in water"></div>
    <h2 class="sheet-title">Investment Management Services – Discretionary</h2>
    <h3 class="sheet-sub">Simplifying investing:<br>with your portfolio managed by professionals</h3>
    <p class="sheet-copy">A bespoke service tailored to your needs, with a dedicated manager taking on the burden of monitoring and</p>
  </article>
  <svg class="pocket" viewBox="0 0 559 765" aria-hidden="true">
    <path d="M26 765 L26 630 Q26 582 74 575 L559 522 L559 765 Z" fill="#ffffff" stroke="#cfcfcf" stroke-width="1"/>
    <path d="M268 596 a14 14 0 0 0 28 0" fill="none" stroke="#aaaaaa" stroke-width="1.4"/>
    <path d="M268 729 a14 14 0 0 1 28 0" fill="none" stroke="#aaaaaa" stroke-width="1.4"/>
  </svg>
</section>

<section class="panel cover-back">
  <div class="brand"><span class="brand-dot"></span>Quelvo</div>
  <div class="contact">
    <p>For application forms, a full set of terms and conditions<br>or for any other enquiry please contact us directly at:</p>
    <p><strong>Quelvo</strong><br>12 Harlow Yard, London, EC2A 7QT<br>Office: +44 (0) 20 7946 0123<br>Dealing line: +44 (0) 20 7946 0456</p>
    <p>www.quelvo.com<br>Email: hello@quelvo.com or for account enquiries: clients@quelvo.com</p>
  </div>
</section>

</body>
</html>
```